VimoraDash Product Logo and Package

***Update*** Please you the text from the attached images on the product design.
Suggested Text:
Logo - VimoraDash
Title - Beta-hydroxybutyrates (BHB)Â Ketone Supplement
Beta-hydroxybutyrates (BHB)Â Ketone Supplement
Beta-hydroxybutyrates (BHB)Â Exogenous Ketones
Beta-hydroxybutyrates (BHB)Â Salts
Instant Ketones
3) Flavor - Orange Mango
4) Servings - 30 Servings 12g BHB Per Serving
5) Seals - Made in USA, FDA Certified Facility, GF (gluten Free), Dairy Free, Keto Friendly, Vegan Friendly, Non-GMO, Naturally Flavored, No Preservatives
6) Uses - Energy, Mental Clarity, Fat Loss, Muscle Strength, Appetite Suppression, Mood Management
7) Big Benefit - Formulated To Induce Rapid Ketosis.
Enjoy the benefits of Ketosis anytime!
50% More Servings Compared To Other Leading Brands!
I would like a logo and package designed for a supplement.
It is a powdered supplement that can be packaged in a plastic jar (8-16 oz) or a bag.
We will also be adding additional products to this line and would like the branding to scale.
The product is packaged in a 16 oz tub.
Product Title: Beta-hydroxybutyrates (BHB) Ketone Supplement
Brand Name: VimoraDash (I'd like the logo image to share the E)
Target Market(s)
Health and Fitness Enthusiasts. Specifically those interested in a Ketogenic Lifestyle.
Industry/Entity Type
Health And Wellness
Requirements
Must have
- Modern, trendy, design.
- Bold colors and fonts.
- Professional but trendy.
- I would like to see Red and Black as the colors used.
Should not have
- Standard, corporate feel.
- Must be fun, engaging, and exciting.

```html
<!DOCTYPE html>
<html lang="en">
<head>
<meta charset="UTF-8">
<title>VimoraDash BHB Ketone Supplement Label</title>
<link rel="stylesheet" href="https://fonts.googleapis.com/css2?family=Arimo:wght@400;700&family=Montserrat:wght@500;600;700&display=swap">
<style>
  :root {
    --page: #ffffff;
    --label-black: #1b1b1b;
    --ink: #2e2a28;
    --white: #ffffff;
    --red: #e8232a;
    --orange: #f47b20;
    --yellow: #fbe316;
    --brand-dot: #f0452a;
  }
  * { margin: 0; padding: 0; box-sizing: border-box; }
  html, body {
    width: 1199px;
    height: 1200px;
    overflow: hidden;
    background: var(--page);
  }
  .canvas {
    position: relative;
    width: 1199px;
    height: 1200px;
  }
  .label {
    position: absolute;
    left: 390px;
    top: 418px;
    width: 668px;
    height: 612px;
    display: flex;
    flex-direction: column;
  }
  .label-top {
    height: 357px;
    background: var(--label-black);
    display: flex;
    align-items: flex-end;
    justify-content: center;
    padding-bottom: 44px;
  }
  .brand {
    display: flex;
    align-items: center;
    gap: 16px;
  }
  .brand-dot {
    width: 30px;
    height: 30px;
    border-radius: 50%;
    background: var(--brand-dot);
  }
  .brand-name {
    font-family: "Montserrat", sans-serif;
    font-weight: 700;
    font-size: 56px;
    letter-spacing: 0.5px;
    color: var(--white);
  }
  .label-band {
    position: relative;
    flex: 1;
    background: linear-gradient(90deg, var(--red) 0%, var(--orange) 25%, var(--yellow) 50%, var(--orange) 75%, var(--red) 100%);
    text-align: center;
    padding-top: 18px;
  }
  .product-title {
    font-family: "Arimo", sans-serif;
    font-weight: 700;
    font-size: 31px;
    line-height: 40px;
    color: var(--ink);
  }
  .type-pill {
    display: inline-block;
    margin-top: 14px;
    padding: 5px 22px;
    border: 2px solid var(--red);
    border-radius: 22px;
    font-family: "Montserrat", sans-serif;
    font-weight: 700;
    font-size: 21px;
    letter-spacing: 1.5px;
    color: var(--red);
  }
  .servings {
    margin-top: 6px;
    font-family: "Montserrat", sans-serif;
    font-weight: 700;
    font-size: 16px;
    color: var(--ink);
  }
  .origin {
    margin-top: 34px;
    font-family: "Montserrat", sans-serif;
    font-weight: 500;
    font-size: 22px;
    color: var(--ink);
  }
  .flavor-badge {
    position: absolute;
    left: 558px;
    top: 138px;
    width: 86px;
    height: 86px;
    border: 3px solid var(--white);
    border-radius: 50%;
    display: flex;
    align-items: center;
    justify-content: center;
    text-align: center;
    font-family: "Montserrat", sans-serif;
    font-weight: 700;
    font-size: 15px;
    line-height: 16px;
    color: var(--white);
  }
</style>
</head>
<body>
  <main class="canvas">
    <section class="label">
      <header class="label-top">
        <div class="brand">
          <span class="brand-dot"></span>
          <span class="brand-name">VimoraDash</span>
        </div>
      </header>
      <div class="label-band">
        <h1 class="product-title">Beta-hydroxybutyrates (BHB)<br>KETONE SUPPLEMENT</h1>
        <div class="type-pill">DIETARY SUPPLIMENT</div>
        <p class="servings">- 30 Servings &nbsp;- 12g BHB</p>
        <p class="origin">MADE IN USA</p>
        <div class="flavor-badge">Orange<br>Mango</div>
      </div>
    </section>
  </main>
</body>
</html>
```